Olive Oil label for bottle 0.5l approx. 10x12 cm

I am running a Spa hotel in Bavaria (logo attached) and my family lives in Greece (Bavarian and Greek flag have the same colors). They produce organic olive oil first cold pressed extra virgin. I would need a label for 0,5 liter bottles to reach them out to my guests and they should see the high quality of the olive oil and the family connection Spa-hotel Bavaria to family in Greece. The name of the family is Morvatek, the hotel is called Tannegg, the olive oil comes from Greece/Argolis/Kranidi. The name of the small olive company is Kerano Hawks. There should be a space for the best before date and the organic control number (handwritten) . The hotel logo is not mandatory. Should look nice 😉

```html
<!DOCTYPE html>
<html lang="en">
<head>
<meta charset="utf-8">
<title>Tannegg – Organic Olive Oil Label</title>
<link href="https://fonts.googleapis.com/css2?family=Comfortaa:wght@700&family=Great+Vibes&family=Open+Sans:wght@400;600&display=swap" rel="stylesheet">
<style>
  :root {
    --backdrop: #b3afb0;
    --paper: #ffffff;
    --ink: #111111;
    --olive-dark: #3b5e2b;
    --olive-mid: #7d9a3a;
    --olive-light: #bccb52;
    --brand-grey: #4c6461;
    --muted: #5d6b5a;
    --rule: #8a9a7c;
    --white: #ffffff;
  }
  html, body {
    margin: 0;
    width: 1200px;
    height: 1200px;
    overflow: hidden;
    background: var(--backdrop);
  }
  .label {
    position: absolute;
    left: 198px;
    top: 116px;
    width: 807px;
    height: 967px;
    background: var(--paper);
    overflow: hidden;
    box-shadow: 4px 4px 8px rgba(0,0,0,0.18);
  }
  .brand {
    position: absolute;
    left: 0;
    right: 0;
    top: 98px;
    margin: 0;
    text-align: center;
    font-family: "Comfortaa", sans-serif;
    font-weight: 700;
    font-size: 74px;
    line-height: 1;
    color: var(--brand-grey);
  }
  .origin {
    position: absolute;
    left: 0;
    right: 0;
    top: 196px;
    margin: 0;
    text-align: center;
    font-family: "Open Sans", sans-serif;
    font-weight: 400;
    font-size: 15px;
    line-height: 1.5;
    letter-spacing: 0.12em;
    text-transform: uppercase;
    color: var(--muted);
  }
  .foliage {
    position: absolute;
    border-radius: 50%;
    background: radial-gradient(circle, rgba(188,203,82,0.75), rgba(125,154,58,0.35) 55%, rgba(255,255,255,0) 72%);
  }
  .branch-art {
    position: absolute;
    left: 383px;
    top: 303px;
    width: 325px;
    height: 500px;
    border-radius: 50%;
    background: radial-gradient(ellipse at 55% 45%, rgba(111,143,52,0.5), rgba(59,94,43,0.22) 55%, rgba(255,255,255,0) 72%);
  }
  .product-name {
    position: absolute;
    left: 233px;
    top: 338px;
    margin: 0;
    font-family: "Comfortaa", sans-serif;
    font-weight: 700;
    color: var(--ink);
    line-height: 1;
  }
  .product-name__line { display: block; }
  .product-name__organic { font-size: 49px; }
  .product-name__olive { font-size: 64px; margin-top: 12px; }
  .product-name__oil {
    font-family: "Great Vibes", cursive;
    font-weight: 400;
    font-size: 230px;
    line-height: 0.8;
    color: var(--olive-dark);
    margin-top: 0;
    margin-left: 40px;
    text-shadow: 6px 10px 10px rgba(0,0,0,0.12);
  }
  .volume-badge {
    position: absolute;
    left: 135px;
    top: 834px;
    width: 534px;
    height: 534px;
    border-radius: 50%;
    background: var(--olive-dark);
  }
  .volume {
    position: absolute;
    left: 135px;
    width: 534px;
    top: 864px;
    margin: 0;
    text-align: center;
    font-family: "Open Sans", sans-serif;
    font-weight: 600;
    font-size: 37px;
    line-height: 1;
    color: var(--white);
  }
  .grade {
    position: absolute;
    left: 135px;
    width: 534px;
    top: 914px;
    margin: 0;
    text-align: center;
    font-family: "Open Sans", sans-serif;
    font-size: 14px;
    letter-spacing: 0.14em;
    text-transform: uppercase;
    color: var(--white);
  }
  .write-in {
    position: absolute;
    top: 880px;
    width: 170px;
    margin: 0;
    font-family: "Open Sans", sans-serif;
    font-size: 13px;
    line-height: 1.3;
    color: var(--muted);
  }
  .write-in--left { left: 28px; }
  .write-in--right { left: 612px; text-align: right; }
  .write-in__field {
    display: block;
    height: 30px;
    border-bottom: 1px solid var(--rule);
  }
</style>
</head>
<body>
  <main class="label">
    <div class="foliage" role="img" aria-label="Olive leaf" style="left:-30px;top:-30px;width:170px;height:150px;"></div>
    <div class="foliage" role="img" aria-label="Blurred olive leaf" style="left:-50px;top:270px;width:170px;height:170px;"></div>
    <div class="foliage" role="img" aria-label="Olive leaf" style="left:-20px;top:560px;width:110px;height:150px;"></div>
    <div class="foliage" role="img" aria-label="Olive leaf" style="left:200px;top:280px;width:80px;height:70px;"></div>
    <div class="foliage" role="img" aria-label="Olive leaf" style="left:690px;top:270px;width:70px;height:120px;"></div>
    <div class="foliage" role="img" aria-label="Blurred olive leaf" style="left:730px;top:630px;width:110px;height:160px;"></div>

    <p class="brand">Tannegg</p>
    <p class="origin">Morvatek family · Kerano Hawks<br>Kranidi · Argolis · Greece</p>

    <div class="branch-art" role="img" aria-label="Olive branch with leaves and green olives"></div>

    <h1 class="product-name">
      <span class="product-name__line product-name__organic">organic</span>
      <span class="product-name__line product-name__olive">oLive</span>
      <span class="product-name__line product-name__oil">oil</span>
    </h1>

    <div class="volume-badge"></div>
    <p class="volume">0.5l</p>
    <p class="grade">Extra virgin · first cold pressed</p>

    <p class="write-in write-in--left">Best before<span class="write-in__field"></span></p>
    <p class="write-in write-in--right">Organic control no.<span class="write-in__field"></span></p>
  </main>
</body>
</html>
```